Corvella Paintless Dent Removal

Our company works on vehicles removing dents using a highly skilled trade which the metal is massaged out with special tools without disturbing the original paint, hence paintless dent removal. Besides keeping the paint and metal original its also very environmentally friendly since no paint or toxic fillers are used. Also we we are one of the most experienced companies in the business with 25 years

Target Market(s)

Retail Automobile consumers, Auto Dealerships and Auto Body Shops

Industry/Entity Type

Auto Repair

Contact Information for Business Card

Dennis Holbrook
PO Box 538 Ashmere, NY 11952
631-472-8816
corvellapdr@mailnest.example
website corvellapdr.example
youtube corvella paintless dent removal
25 years of experience removing Dents, Dings and Hail Damage

Font styles to use
Serif
Sans Serif

Colors

Designer to choose colors to be used in the design.

Requirements
Must have
• I do like things that are simple but classy and somewhat bold, also I like my logo so that should be somewhat important

```html
<!DOCTYPE html>
<html lang="en">
<head>
<meta charset="utf-8">
<title>Corvella Paintless Dent Removal – Business Card</title>
<link href="https://fonts.googleapis.com/css2?family=Open+Sans:ital,wght@0,400;0,700;0,800;1,400&display=swap" rel="stylesheet">
<style>
  :root {
    --navy: #323e5c;
    --green: #7dc400;
    --white: #ffffff;
    --ink: #2b3550;
    --backdrop: #d9dadc;
  }
  * { margin: 0; padding: 0; box-sizing: border-box; }
  html, body {
    width: 1200px; height: 801px; overflow: hidden;
    background: var(--backdrop);
    font-family: "Open Sans", Arial, sans-serif;
  }
  .card {
    position: absolute; left: 100px; top: 115px;
    width: 1000px; height: 570px;
    background: var(--white);
    border-radius: 34px;
    overflow: hidden;
    box-shadow: 0 10px 30px rgba(0,0,0,.25);
  }
  .brand {
    position: absolute; left: 50px; top: 82px;
    display: flex; align-items: center; gap: 20px;
    color: var(--navy); font-weight: 800;
  }
  .brand-dot { width: 28px; height: 28px; border-radius: 50%; background: var(--green); flex: none; }
  .brand-name { line-height: 1.05; }
  .brand-name .word { display: block; font-size: 58px; letter-spacing: 1px; text-transform: uppercase; }
  .brand-name .tag { display: block; font-size: 22px; margin-top: 4px; }
  .holder {
    position: absolute; left: 562px; top: 104px;
    font-size: 31px; font-weight: 700; color: var(--ink);
  }
  .contacts {
    position: absolute; left: 525px; top: 196px;
    list-style: none;
  }
  .contacts li {
    display: flex; align-items: center; gap: 14px;
    height: 38px; font-size: 26px; color: var(--ink);
  }
  .contacts svg { width: 22px; height: 22px; flex: none; }
  .band { position: absolute; left: 0; top: 412px; width: 1000px; height: 114px; }
  .band-text {
    position: absolute; left: 408px; top: 418px;
    color: var(--white); font-style: italic; font-size: 26px; line-height: 36px;
  }
</style>
</head>
<body>
<main class="card">
  <div class="brand">
    <span class="brand-dot"></span>
    <span class="brand-name"><span class="word">Corvella</span><span class="tag">Paintless Dent Removal</span></span>
  </div>

  <h1 class="holder">Dennis Holbrook</h1>

  <ul class="contacts">
    <li><svg viewBox="0 0 22 22"><circle cx="11" cy="11" r="11" fill="var(--green)"/><rect x="6" y="7" width="10" height="8" rx="1" fill="#fff"/></svg>PO Box 538</li>
    <li><svg viewBox="0 0 22 22"><circle cx="11" cy="11" r="11" fill="var(--green)"/><path d="M11 4a4 4 0 0 1 4 4c0 3-4 8-4 8s-4-5-4-8a4 4 0 0 1 4-4z" fill="#fff"/><circle cx="11" cy="8" r="1.5" fill="var(--green)"/></svg>Ashmere, NY 11952</li>
    <li><svg viewBox="0 0 22 22"><circle cx="11" cy="11" r="11" fill="var(--green)"/><path d="M7 6h3l1 3-2 1a7 7 0 0 0 3 3l1-2 3 1v3c-6 0-9-3-9-9z" fill="#fff"/></svg>631-472-8816</li>
    <li><svg viewBox="0 0 22 22"><circle cx="11" cy="11" r="11" fill="var(--green)"/><rect x="5" y="7" width="12" height="8" fill="#fff"/><path d="M5 7l6 5 6-5" stroke="var(--green)" stroke-width="1.2" fill="none"/></svg>corvellapdr@mailnest.example</li>
    <li><svg viewBox="0 0 22 22"><circle cx="11" cy="11" r="11" fill="var(--green)"/><circle cx="11" cy="11" r="6" fill="none" stroke="#fff" stroke-width="1.4"/><path d="M5 11h12M11 5v12" stroke="#fff" stroke-width="1.2"/></svg>website corvellapdr.example</li>
  </ul>

  <svg class="band" viewBox="0 0 1000 114" aria-hidden="true">
    <path d="M0 0h200q40 0 40 40v74H0z" fill="var(--navy)"/>
    <path d="M218 0H1000V114H262z" fill="var(--green)"/>
  </svg>
  <p class="band-text">Youtube Corvella Paintless Dent Removal<br>25 Years Of Experience Removing Dents,<br>Dings and Hail Damage</p>
</main>
</body>
</html>
```